2 page flyer outlining details of a product framework

We need a flyer for a management consulting firm outlining a product we offer. The draft wording and company logo are attached. Logo colours should be used (Purple - C73, M93, Y0, K0 & Green - C50, M0, Y99, K0).
The look and feel should communicate a dynamic, trustworthy, credible organisation with excellence in delivery.

File must be provided in AI format to enable text changes.

Target Market(s)

Senior Business Excecutives

Industry/Entity Type

Management Consulting

Font styles to use
Other font styles liked:
• Aller & Myriad Pro

Colors
acd036
6b449b

Requirements
Must have
• Logo & wording provided, professional images and a flyer layout with space and a section for contact details.

```html
<!DOCTYPE html>
<html lang="en">
<head>
<meta charset="utf-8">
<title>FLOW! Framework Assessment – Flyer</title>
<link rel="stylesheet" href="https://fonts.googleapis.com/css2?family=PT+Sans:wght@400;700&family=PT+Sans+Narrow:wght@400;700&display=swap">
<style>
  :root {
    --purple: #6b449b;
    --purple-deep: #5e3790;
    --green: #acd036;
    --green-text: #8cc63f;
    --ink: #3a2a55;
    --grey: #8a8a8a;
    --rule: #9a9a9a;
    --paper: #ffffff;
    --stage: #ffffff;
  }
  * { margin: 0; padding: 0; box-sizing: border-box; }
  html, body { width: 1200px; height: 1000px; overflow: hidden; background: var(--stage); }
  body { position: relative; font-family: "PT Sans", Arial, sans-serif; color: var(--ink); }

  .page { position: absolute; box-shadow: 4px 6px 14px rgba(0,0,0,.28); overflow: hidden; }

  /* ---------- Cover page ---------- */
  .cover { left: 27px; top: 105px; width: 546px; height: 772px; background: var(--purple); color: #fff; }
  .cover__title {
    position: absolute; left: 0; right: 0; top: 82px; text-align: center;
    font-family: "PT Sans", Arial, sans-serif; font-weight: 700; font-size: 176px;
    line-height: 1; letter-spacing: -4px; color: #fff;
  }
  .cover__subtitle {
    position: absolute; left: 0; right: 0; top: 240px; text-align: center;
    font-family: "PT Sans Narrow", Arial, sans-serif; font-size: 17.5px; color: var(--green);
    letter-spacing: .2px;
  }
  .cover__copy { position: absolute; left: 82px; top: 323px; width: 230px; }
  .cover__question { font-size: 18.5px; line-height: 24px; margin-bottom: 12px; }
  .cover__question strong { font-weight: 700; }
  .cover__answer { font-size: 18.5px; line-height: 22px; color: var(--green); margin-top: 6px; }
  .cover__answer strong { font-weight: 700; }
  .cover__body {
    margin-top: 18px; width: 180px; font-family: "PT Sans Narrow", Arial, sans-serif;
    font-size: 12.5px; line-height: 15.5px;
  }

  /* ---------- Detail page ---------- */
  .detail { left: 606px; top: 107px; width: 539px; height: 766px; background: var(--paper); }
  .contact { position: absolute; left: 28px; top: 68px; font-family: "PT Sans Narrow", Arial, sans-serif; font-size: 15.5px; line-height: 20px; color: var(--purple); }
  .contact__label { color: var(--green-text); }
  .contact__row span { display: inline-block; width: 26px; }

  .brand { position: absolute; right: 30px; top: 70px; display: flex; align-items: center; gap: 8px; }
  .brand__dot { width: 18px; height: 18px; border-radius: 50%; background: var(--green); }
  .brand__name { font-family: "PT Sans", Arial, sans-serif; font-weight: 700; font-size: 24px; color: var(--purple); letter-spacing: .5px; }

  .rule { position: absolute; left: 28px; width: 481px; height: 1px; background: var(--rule); }
  .rule--top { top: 159px; }
  .rule--bottom { top: 703px; }

  .col { position: absolute; top: 176px; }
  .col--areas { left: 28px; width: 228px; }
  .col--process { left: 281px; width: 228px; }

  .col__heading { font-family: "PT Sans Narrow", Arial, sans-serif; font-size: 16px; line-height: 18px; color: var(--green-text); margin-bottom: 14px; }
  .col__heading strong { font-weight: 700; }

  .area { margin-bottom: 6px; }
  .area__num { font-family: "PT Sans Narrow", Arial, sans-serif; font-size: 18px; line-height: 16px; color: var(--purple); }
  .area__title { font-size: 8.2px; line-height: 10.5px; font-weight: 700; color: var(--purple); }
  .small { font-size: 7.4px; line-height: 10.5px; color: #333; }
  .list { list-style: none; }
  .list li { position: relative; padding-left: 14px; font-size: 7.4px; line-height: 10.5px; color: #333; }
  .list li::before { content: "•"; position: absolute; left: 0; }

  .process p { margin-bottom: 8px; }
  .phase__title { font-size: 8.2px; font-weight: 700; color: var(--purple); margin: 8px 0 2px; }
  .price { font-family: "PT Sans Narrow", Arial, sans-serif; font-size: 15px; line-height: 17px; color: var(--green-text); margin-top: 18px; }
  .price strong { font-weight: 700; }
  .price + .price { margin-top: 8px; }

  .cta { position: absolute; left: 28px; top: 670px; width: 481px; font-family: "PT Sans Narrow", Arial, sans-serif; font-size: 20px; color: var(--green-text); }
  .notes { position: absolute; left: 28px; top: 710px; width: 490px; list-style: none; }
  .notes li { position: relative; padding-left: 10px; font-size: 5.6px; line-height: 8px; color: var(--grey); }
  .notes li::before { content: "•"; position: absolute; left: 0; }
</style>
</head>
<body>

<section class="page cover">
  <h1 class="cover__title">FLOW!</h1>
  <p class="cover__subtitle">FULLY LEVERAGED OPTIMISED WORKFORCE (FLOW!) FRAMEWORK ASSESSMENT</p>
  <div class="cover__copy">
    <p class="cover__question">How <strong>much</strong> is inefficient workforce management <strong>costing</strong> your business?</p>
    <p class="cover__question">Are you as <strong>efficient</strong> as you could be?</p>
    <p class="cover__answer">Find the answers with a powerful <strong>Fully Leveraged Optimised Workforce ™ (FLOW!) Framework Assessment!</strong></p>
    <p class="cover__body">We provide a detailed, tailored assessment based on our proprietary <strong>FLOW! Framework</strong>. Our framework is scalable and flexible to suit organisations of any size and structure – providing you with a roadmap to successfully achieving better business outcomes, greater efficiency, and cost savings.</p>
  </div>
</section>

<section class="page detail">
  <div class="contact">
    <p class="contact__label">Contact us</p>
    <p class="contact__row"><span>T:</span>0255 010 000</p>
    <p class="contact__row"><span>E:</span>hello@corvale.com</p>
    <p>www.corvale.co.uk</p>
  </div>

  <div class="brand">
    <span class="brand__dot"></span>
    <span class="brand__name">CORVALE ADVISORY</span>
  </div>

  <div class="rule rule--top"></div>

  <div class="col col--areas">
    <h2 class="col__heading">Our <strong>FLOW! Framework Assessment</strong><br>looks at the following key areas;</h2>

    <div class="area">
      <p class="area__num">1</p>
      <p class="area__title">Planning Capability – how well do you predict and plan for the future?</p>
      <p class="small">We review how you approach forecasting and scheduling activities, including;</p>
      <ul class="list"><li>Data accuracy and validity</li><li>Known variations (i.e. Public Holidays &amp; Marketing activities)</li><li>Assumptions used in the planning process</li></ul>
    </div>
    <div class="area">
      <p class="area__num">2</p>
      <p class="area__title">Real Time Management – how well do you respond to changing needs and unexpected events?</p>
      <p class="small">We review how you manage intraday activities, including;</p>
      <ul class="list"><li>Reforecasting and planning</li><li>Managing exceptions</li><li>Recovery strategies</li></ul>
    </div>
    <div class="area">
      <p class="area__num">3</p>
      <p class="area__title">System Interaction and Acceptance – how well have you enabled and empowered your team to get the most out of the system?</p>
      <p class="small">We review how you utilise and enable capabilities such as;</p>
      <ul class="list"><li>Use of self-service functionality</li><li>Use of meeting and training scheduling functionality</li><li>Support team autonomy and interaction with the system</li></ul>
    </div>
    <div class="area">
      <p class="area__num">4</p>
      <p class="area__title">Reporting – how well are you using the valuable data available to make informed business decisions?</p>
      <p class="small">We review how you utilise available reports and data, including;</p>
      <ul class="list"><li>Information currently reported</li><li>Inclusion of workforce management metrics in management reports</li><li>Accuracy and validity of reported metrics</li></ul>
    </div>
  </div>

  <div class="col col--process process">
    <h2 class="col__heading">You may be wondering what is involved in the <strong>FLOW! Framework Assessment?</strong></h2>
    <p class="small">To keep your team hard at work doing what they do best, we conduct our <strong>FLOW! Framework Assessment</strong> in just a few interviews over a 2-day site visit. For larger and multi-site organisations we also use online surveys to increase the amount of data we can capture with minimal business disruption.</p>
    <p class="small">A typical FLOW! Framework Assessment is structured over a number of phases;</p>

    <p class="phase__title">Phase 1 - Analysis</p>
    <ul class="list">
      <li>Survey designed and distributed</li>
      <li>Initial briefing with Contact Centre Manager</li>
      <li>Detailed overview of workforce management system and processes with Workforce Management team members</li>
      <li>Interviews with Team Leaders</li>
      <li>Interviews with Quality Assurance team members</li>
      <li>Interviews with Training team members</li>
      <li>Interviews with frontline staff</li>
      <li>Follow up discussions with Workforce Management team members as required</li>
    </ul>
    <p class="phase__title">Phase 2 – Report Development</p>
    <ul class="list">
      <li>Development of initial report of findings</li>
      <li>Discussions with solution vendor (where available) to confirm system capability in addressing key problem areas identified</li>
      <li>Development of final report including recommendations for enhancement</li>
    </ul>
    <p class="phase__title">Phase 3 – Report Delivery</p>
    <ul class="list">
      <li>Delivery of final report including observations and key recommendations</li>
    </ul>

    <p class="price">Full package price =<br><strong>$10,000 (ex GST)</strong></p>
    <p class="price">25% discount for key customers =<br><strong>$7,500 (ex GST)</strong></p>
  </div>

  <p class="cta">Call Corvale Advisory to book in for your assessment today!</p>
  <div class="rule rule--bottom"></div>
  <ul class="notes">
    <li>Discount offer valid until 30th June 2015, unless sold out prior.</li>
    <li>FLOW! Framework Assessment structure is indicative and may vary for each organisation.</li>
    <li>Package price includes 2 days on-site plus report preparation, which is suitable for a small to medium sized contact centre with a centralised workforce management team. Larger clients or those with decentralised workforce management teams may request extra on-site days for an additional fee.</li>
  </ul>
</section>

</body>
</html>
```